Web Design Job: Condo Debts Collection Business needs a Web Design

I need a site for a client, who works with condo debts collection, and ensure all revenues provided by condo fees will be always available to the building manager of condo on a specific date, regardless of defaults.
I have the visual identity (logo, slogan and colors) of the company, and some requirements on layout (kind of slider, menu options, phone number on a noble position, etc) - maybe I can do a sketch, but I like the idea of give some freedom to designer.

*** PLEASE, we have no interest in templates. We want something new***
Updates

Reason: We need something new, different and exclusive. We do not want anything that looks like a "template". Thanks.

Target Market(s)

I have two targets for this design:
- Condominium's building manager. This target is looking for a solution to overdue debts on it's condo.
- Residents on condominiums. This target wants to live in a better place, where their neighbors pay their condominium fees on time.

Industry/Entity Type

Business

Number of Pages Required

1 page

Requirements
Must have
• - Slider with title, some short text related, a nice image (I prefer happy and/or peaceful family, people doing business, happy friends, and so on).
• - I have a special attention to menu. I'm looking for one I can have a nice effect, more elegant, charming, kind of innovative.
• - Phone number on the top (or clearly visible).
• - Member log in area or icon on the top (or clearly visible).
• - News/articles area.
• - Modern fonts, with good quality, sans-serif on areas where reading is more intensive (prefer Google web-fonts).
• - Colors specified on attached files.
Nice to have
• - Clear background color, cause it's better to read larger texts (like articles). Dark backgrounds makes reading difficult.
• - A site with effects (like shadows, lines, curves, gradients, lights) is usually pretty.
• - I pay attention on beautiful footers.
Should not have
• - Images with a lot of money (I don't sell richness, I sell tranquility, peace, harmony, safety).
• - Poor menu.

```html
<!DOCTYPE html>
<html lang="pt">
<head>
<meta charset="utf-8">
<title>Condara Solução Cobrança</title>
<link rel="stylesheet" href="https://fonts.googleapis.com/css2?family=Raleway:wght@400;500;600&family=Open+Sans:wght@400;600&display=swap">
<style>
:root{
  --navy:#1b2766;
  --navy-deep:#131c4d;
  --navy-mid:#243586;
  --nav:#2b43a3;
  --nav-dark:#1d2e7c;
  --red:#d0282e;
  --ink:#1e2a5e;
  --text:#5a5a5a;
  --muted:#8a8a8a;
  --white:#fff;
  --line:#e4e6ec;
}
*{margin:0;padding:0;box-sizing:border-box}
html,body{width:859px;height:1200px;overflow:hidden;background:var(--white)}
body{position:relative;font-family:"Open Sans",sans-serif;color:var(--text)}
.abs{position:absolute}
.header-band{left:0;top:0;width:859px;height:166px;background:linear-gradient(#25357f,#182460 70%,#141e52)}
.brand{left:138px;top:0;width:146px;height:72px;background:rgba(255,255,255,.05);display:flex;flex-direction:column;align-items:center;justify-content:center;gap:4px;color:var(--white);font-family:"Raleway",sans-serif}
.brand-name{font-size:17px;font-weight:600;letter-spacing:1px}
.brand-tag{font-size:6px;font-weight:600;letter-spacing:1px}
.member-login{left:638px;top:0;width:82px;height:24px;background:var(--navy-deep);color:#dfe3f3;font-size:7.5px;display:flex;align-items:center;justify-content:center;gap:4px}
.phone-label{right:139px;top:40px;color:var(--white);font-size:7.5px}
.phone-number{right:139px;top:48px;color:var(--white);font-size:14px;font-family:"Raleway",sans-serif;font-weight:500;display:flex;align-items:center;gap:3px}
.main-nav{left:138px;top:74px;width:584px;height:38px;background:linear-gradient(#3350b6,var(--nav-dark));border-top:2px solid #4762c8;display:flex}
.main-nav a{display:flex;align-items:center;justify-content:center;color:var(--white);text-decoration:none;font-family:"Raleway",sans-serif;font-size:11px;font-weight:500;border-right:1px solid #1a2865;box-shadow:1px 0 0 #4460c2}
.main-nav a:last-child{border:none;box-shadow:none}
.slider{left:138px;top:112px;width:584px;height:262px;border-radius:0 0 4px 4px;background:linear-gradient(135deg,#7fa560 0%,#d9b7a0 35%,#c98fb0 55%,#9fb3cf 75%,#e3e4ea 100%);box-shadow:0 10px 18px rgba(0,0,0,.12)}
.slide-caption{left:138px;top:205px;width:251px;height:77px;background:rgba(53,73,160,.85);color:var(--white);padding:13px 16px}
.slide-caption h2{font-family:"Raleway",sans-serif;font-weight:500;font-size:18.5px;margin-bottom:4px}
.slide-caption p{font-family:"Raleway",sans-serif;font-size:9.5px;line-height:14px}
.slider-dots{left:405px;top:352px;display:flex;gap:4px}
.slider-dots span{width:11px;height:11px;border-radius:50%;background:var(--white)}
.about h1{position:absolute;left:0;top:420px;width:859px;text-align:center;font-family:"Raleway",sans-serif;font-weight:400;font-size:20.5px;color:#1c1c2a;letter-spacing:.3px}
.about-text{left:166px;top:454px;width:530px;text-align:center;font-size:7px;line-height:12px}
.about-text p{margin-bottom:7px}
.divider{left:138px;top:564px;width:584px;height:1px;background:var(--line)}
.feature-img{width:148px;height:92px;top:606px}
.feature h3{position:absolute;font-family:"Raleway",sans-serif;font-weight:500;font-size:14.5px;color:var(--ink)}
.feature p{position:absolute;width:126px;font-size:7px;line-height:11.2px;color:var(--muted)}
.btn{position:absolute;height:20px;width:66px;background:linear-gradient(#2b3f96,var(--navy));color:var(--white);font-size:7px;font-weight:600;display:flex;align-items:center;justify-content:center;border-radius:2px}
.soft-line{left:20px;top:731px;width:819px;height:1px;background:#eef0f3}
.news-title{left:143px;top:770px;font-family:"Raleway",sans-serif;font-weight:500;font-size:16.5px;color:var(--ink)}
.news-img{width:77px;height:50px}
.news-item h4{position:absolute;font-size:9px;font-weight:400;color:var(--red)}
.news-item p{position:absolute;width:185px;font-size:7px;line-height:12.8px;color:var(--muted)}
.footer{left:0;top:976px;width:859px;height:178px;background:linear-gradient(#2a3a86,#1d2a6b 60%,#182360)}
.footer-col h5{position:absolute;top:1007px;font-family:"Raleway",sans-serif;font-weight:400;font-size:13px;color:#c5cbe6}
.footer-col ul{position:absolute;top:1032px;list-style:none;font-size:8.2px;color:#e3e6f3;line-height:16.8px}
.badge{left:534px;top:1094px;width:102px;height:40px;background:var(--white)}
.bottom-bar{left:0;top:1154px;width:859px;height:46px;background:var(--navy-deep)}
.copyright{left:143px;top:1170px;font-size:6.5px;color:#a9b0d3}
.social{left:659px;top:1170px;display:flex;gap:4px}
.social span{width:12px;height:12px;border-radius:2px;background:#e9ecf7}
</style>
</head>
<body>
<div class="abs header-band"></div>
<div class="abs brand"><span class="brand-name">Condara</span><span class="brand-tag">SOLUÇÃO COBRANÇA</span></div>
<div class="abs member-login">
  <svg width="8" height="8" viewBox="0 0 10 10"><circle cx="5" cy="3" r="2.4" fill="#fff"/><path d="M0.5 10a4.5 4 0 0 1 9 0z" fill="#fff"/></svg>Member Login
</div>
<div class="abs phone-label">Phone Support</div>
<div class="abs phone-number">
  <svg width="10" height="10" viewBox="0 0 24 24"><path fill="#fff" d="M6.6 10.8a15 15 0 0 0 6.6 6.6l2.2-2.2c.3-.3.7-.4 1-.2 1.1.4 2.3.6 3.6.6.6 0 1 .4 1 1V20c0 .6-.4 1-1 1C10.6 21 3 13.4 3 4c0-.6.4-1 1-1h3.5c.6 0 1 .4 1 1 0 1.3.2 2.5.6 3.6.1.3 0 .7-.2 1z"/></svg>555.201.4830
</div>
<nav class="abs main-nav">
  <a style="width:90px">HOME</a><a style="width:100px">ABOUT US</a><a style="width:100px">SERVICES</a><a style="width:108px">RESOURCES</a><a style="width:84px">NEWS</a><a style="width:102px">CONTACT</a>
</nav>
<div class="abs slider" role="img" aria-label="Photo of a smiling multi-generation family sitting together outdoors"></div>
<div class="abs slide-caption"><h2>Proin nulla arcu nonummy</h2><p>Morbi ornare gravida elit Integer congue augue et malesuada iaculis</p></div>
<div class="abs slider-dots"><span></span><span></span><span></span><span></span></div>

<section class="about">
  <h1>ABOUT OUR COMPANY</h1>
  <div class="abs about-text">
    <p>A CONDARA SOLUÇÃO COBRANÇA é uma empresa que faz a cobrança do seu condomínio de forma diferente. Todo mês, na data de vencimento das taxas condominiais depositamos na conta bancária do condomínio o valor da receita total (descontada nossa taxa de serviço), efetuando posteriormente a cobrança daqueles que não pagaram em dia. Se algum condômino deixa de pagar, a Condara assume essa obrigação e paga a taxa de condomínio por ele.</p>
    <p>A Condara busca melhorar a gestão do condomínio através da solução do problema da falta de dinheiro. Afinal, não é o sonho de todo síndico receber em dia e não se preocupar em cobrar seus vizinhos?</p>
  </div>
</section>
<div class="abs divider"></div>

<section class="feature">
  <div class="abs feature-img" style="left:137px;background:linear-gradient(135deg,#9fb4cf,#5f6f86)" role="img" aria-label="Photo of two businessmen discussing documents in an office"></div>
  <h3 style="left:296px;top:603px">What We Do</h3>
  <p style="left:296px;top:625px">Vivamus porttitor purus nisi eleifend libero a tempus libero lectus feugiat felis Morbi diam mauris viverra in gravida eu mattis in ante</p>
  <div class="btn" style="left:297px;top:674px">READ MORE</div>
  <div class="abs feature-img" style="left:439px;background:linear-gradient(135deg,#e7e8ec,#a9acb5)" role="img" aria-label="Photo of a smiling businesswoman with arms crossed"></div>
  <h3 style="left:598px;top:603px">Services Provides</h3>
  <p style="left:598px;top:625px">Vivamus porttitor purus nisi eleifend libero a tempus libero lectus feugiat felis Morbi diam mauris viverra in gravida eu mattis in ante</p>
  <div class="btn" style="left:602px;top:674px">READ MORE</div>
</section>
<div class="abs soft-line"></div>

<h2 class="abs news-title">News &amp; Articles</h2>
<section class="news-item">
  <div class="abs news-img" style="left:144px;top:806px;background:linear-gradient(135deg,#e4dccb,#9a8f7d)" role="img" aria-label="Photo of an approved debt relief application form"></div>
  <h4 style="left:230px;top:805px">Morbi diam mauris viverra</h4>
  <p style="left:230px;top:818px">Vivamus porttitor purus nisi eleifend libero a tempus libero lectus feugiat felis Morbi diam mauris viverra in gravida eu mattis in ante Morbi eget</p>
  <div class="abs news-img" style="left:449px;top:805px;background:linear-gradient(135deg,#eef0f4,#7d9cc4)" role="img" aria-label="Photo of a smiling woman in a denim shirt"></div>
  <h4 style="left:534px;top:804px">Morbi diam mauris viverra</h4>
  <p style="left:534px;top:817px">Vivamus porttitor purus nisi eleifend libero a tempus libero lectus feugiat felis Morbi diam mauris viverra in gravida eu mattis in ante Morbi eget</p>
  <div class="abs news-img" style="left:144px;top:878px;background:linear-gradient(135deg,#d8d8d8,#8e8e8e)" role="img" aria-label="Photo of financial papers with a red pen"></div>
  <h4 style="left:230px;top:876px">Cum sociis natoque penatibus et</h4>
  <p style="left:230px;top:889px">Vivamus porttitor purus nisi eleifend libero a tempus libero lectus feugiat felis Morbi diam mauris viverra in gravida eu mattis in ante Morbi eget</p>
  <div class="abs news-img" style="left:449px;top:877px;background:linear-gradient(135deg,#e8c45a,#9aa6b8)" role="img" aria-label="Photo of a couple meeting with an advisor"></div>
  <h4 style="left:534px;top:875px">Cum sociis natoque penatibus et</h4>
  <p style="left:534px;top:888px">Vivamus porttitor purus nisi eleifend libero a tempus libero lectus feugiat felis Morbi diam mauris viverra in gravida eu mattis in ante Morbi eget</p>
</section>

<footer>
  <div class="abs footer"></div>
  <div class="footer-col"><h5 style="left:143px">Company</h5><ul style="left:143px"><li>Our Vision</li><li>About Us</li><li>Products</li><li>Tech Support</li><li>Construction</li></ul></div>
  <div class="footer-col"><h5 style="left:258px">Services</h5><ul style="left:259px"><li>Class aptent taciti</li><li>Sociosqu ad</li><li>Aitora torquent</li><li>Per conubia</li><li>Nostra per</li></ul></div>
  <div class="footer-col"><h5 style="left:393px">Services</h5><ul style="left:393px"><li>Class aptent taciti</li><li>Sociosqu ad</li><li>Aitora torquent</li><li>Per conubia</li><li>Nostra per</li></ul></div>
  <div class="footer-col"><h5 style="left:532px">Contact Info</h5><ul style="left:533px"><li>48 Harbor Lane #4B Austin 73301 TX</li><li>Phone: 555.317.0946</li><li>Email: info@condara-example.com</li></ul></div>
  <div class="abs badge"></div>
  <div class="abs bottom-bar"></div>
  <div class="abs copyright">© 2015 Company Name &nbsp;All right reserved &nbsp;Term of Use</div>
  <div class="abs social"><span></span><span></span><span></span></div>
</footer>
</body>
</html>
```